Mezzanine Floor Manufacturer looking for a new business card design

We manufacture mezzanine floors and are providers of racking systems. We provide a range of items/services - simple rack repairs , full warehouse fit outs , manufacturer and install mezzanine floors , partitioning and large turnkey projects. Recently had a new website - www.corvane-shelving.co.uk and would like our business cards updating aswell . Our current card is single sided in the old logo colours (pdf attached) and needs updating.

Target Market(s)

We deal with large projects/ multi national companies and also smaller projects and companies throughout the UK ranging from a single warehouse to a large multi site company.

Industry/Entity Type

Business

Contact Information for Business Card

Will have job title,tel no's, email ,website address etc like example pdf

Requirements
Must have
• Hi - needs to use the colours of the logo & new website. Card needs to be professional

```html
<!DOCTYPE html>
<html lang="en">
<head>
<meta charset="utf-8">
<title>Corvane Business Card</title>
<link href="https://fonts.googleapis.com/css2?family=Lato:wght@400;700&display=swap" rel="stylesheet">
<style>
  :root {
    --brand-red: #dc2a1c;
    --paper: #ffffff;
    --backdrop: #e6e6e6;
    --silver-light: #f2f2f2;
    --silver-dark: #a9a9a9;
    --card-w: 510px;
    --card-h: 291px;
  }
  * { margin: 0; padding: 0; box-sizing: border-box; }
  html, body {
    width: 1200px; height: 675px; overflow: hidden;
    background: var(--backdrop);
    font-family: 'Lato', sans-serif;
  }
  .canvas {
    position: relative; width: 1200px; height: 675px;
    display: flex; align-items: center; justify-content: center; gap: 50px;
  }
  .card {
    position: relative; width: var(--card-w); height: var(--card-h);
    overflow: hidden; box-shadow: 0 6px 18px rgba(0,0,0,0.18);
  }
  .card-front {
    background: var(--brand-red); color: var(--paper);
    display: flex; flex-direction: column; align-items: center; justify-content: center;
  }
  .brand-name {
    font-weight: 700; font-size: 52px; letter-spacing: 1px; line-height: 1;
  }
  .card-front .brand-name { color: var(--paper); margin-top: 10px; }
  .front-url {
    margin-top: 46px; font-size: 14px; letter-spacing: 2.6px;
  }
  .card-back { background: var(--paper); }
  .card-back .shape { position: absolute; inset: 0; }
  .card-back .brand-name {
    position: absolute; right: 34px; top: 104px;
    color: var(--brand-red); font-size: 40px;
  }
  .contact {
    position: absolute; left: 40px; top: 46px; color: var(--paper);
  }
  .person-name { font-size: 18px; font-weight: 400; }
  .person-role { font-size: 12px; margin-left: 8px; }
  .address { margin-top: 20px; margin-left: 20px; font-size: 13px; line-height: 1.35; }
  .contact-list { list-style: none; margin-top: 14px; margin-left: 20px; font-size: 13px; }
  .contact-list li { display: flex; align-items: center; gap: 8px; line-height: 1.45; }
  .contact-list svg { width: 12px; height: 12px; flex: none; }
</style>
</head>
<body>
<main class="canvas">
  <section class="card card-front" aria-label="Card front">
    <div class="brand-name">Corvane</div>
    <div class="front-url">www.corvane-shelving.co.uk</div>
  </section>

  <section class="card card-back" aria-label="Card back">
    <svg class="shape" viewBox="0 0 510 291" aria-hidden="true">
      <defs>
        <linearGradient id="silverSweep" x1="0" y1="1" x2="1" y2="0">
          <stop offset="0" stop-color="var(--silver-dark)"/>
          <stop offset="0.5" stop-color="var(--silver-light)"/>
          <stop offset="1" stop-color="var(--silver-dark)"/>
        </linearGradient>
      </defs>
      <path d="M0 0 H318 C338 120 310 225 232 291 H0 Z" fill="url(#silverSweep)"/>
      <path d="M0 0 H310 C326 110 292 210 208 291 H0 Z" fill="var(--brand-red)"/>
      <path d="M208 291 C262 240 288 195 300 150 C292 205 266 250 232 291 Z" fill="url(#silverSweep)"/>
    </svg>

    <div class="contact">
      <div class="person-name">Mara Kellow</div>
      <div class="person-role">Manager</div>
      <div class="address">1450 Holt Lane<br>Ashby TX 78010</div>
      <ul class="contact-list">
        <li>
          <svg viewBox="0 0 12 12" aria-hidden="true"><path d="M3 1 L5 3.5 L4 5 C4.6 6.4 5.6 7.4 7 8 L8.5 7 L11 9 L9.8 11 C5 10.6 1.4 7 1 2.2 Z" fill="none" stroke="#fff" stroke-width="1"/></svg>
          512 004 2210
        </li>
        <li>
          <svg viewBox="0 0 12 12" aria-hidden="true"><rect x="1" y="5" width="10" height="6" fill="#fff"/><rect x="3" y="1" width="6" height="4" fill="none" stroke="#fff"/></svg>
          512 004 2211
        </li>
        <li>
          <svg viewBox="0 0 12 12" aria-hidden="true"><rect x="1" y="3" width="10" height="7" fill="#fff"/><path d="M1 3 L6 7 L11 3" fill="none" stroke="var(--brand-red)"/></svg>
          info@fernleyfinance.com
        </li>
        <li>
          <svg viewBox="0 0 12 12" aria-hidden="true"><circle cx="6" cy="6" r="5" fill="none" stroke="#fff"/><path d="M1 6 H11 M6 1 V11 M6 1 C3 4 3 8 6 11 M6 1 C9 4 9 8 6 11" fill="none" stroke="#fff" stroke-width="0.8"/></svg>
          www.fernleyfinance.com
        </li>
      </ul>
    </div>

    <div class="brand-name">Corvane</div>
  </section>
</main>
</body>
</html>
```